Korvane Pty Ltd professional business card

A professional business card template using the colours from the supplied logo.
Clean crisp lines while, Modern while not being over the top.

Target Market(s)

Construction, commerical and industrial

Industry/Entity Type

Communications

Contact Information for Business Card

For a Communications, IT, Optical fibre installation company

Colors
37b8a4

```html
<!DOCTYPE html>
<html lang="en">
<head>
<meta charset="utf-8">
<title>Korvane Pty Ltd – Business Card</title>
<link href="https://fonts.googleapis.com/css2?family=Open+Sans:wght@400;600&display=swap" rel="stylesheet">
<style>
  :root {
    --stage: #d9d9da;
    --card-white: #ffffff;
    --card-grey: #6a6b6d;
    --teal: #1e959b;
    --ink-grey: #5d5e60;
    --text-light: #ffffff;
    --text-soft: #e6e6e7;
  }
  html, body {
    margin: 0;
    width: 1200px;
    height: 800px;
    overflow: hidden;
    background: var(--stage);
    font-family: "Open Sans", Arial, sans-serif;
  }
  .stage {
    width: 1200px;
    height: 800px;
    display: flex;
    align-items: center;
    justify-content: center;
    gap: 40px;
  }
  .card {
    position: relative;
    width: 530px;
    height: 303px;
    border-radius: 16px;
    overflow: hidden;
    box-shadow: 0 4px 14px rgba(0,0,0,0.18);
  }
  .card-front { background: var(--card-white); }
  .card-back {
    background: var(--card-grey);
    display: flex;
    align-items: center;
    justify-content: center;
  }
  .front-shapes { position: absolute; inset: 0; }
  .holder {
    position: absolute;
    left: 30px;
    top: 96px;
    color: var(--text-light);
  }
  .holder-name { font-size: 19px; font-weight: 400; margin: 0; line-height: 1.2; }
  .holder-title { font-size: 11px; color: var(--text-soft); margin: 2px 0 0; }
  .contact-list {
    position: absolute;
    left: 30px;
    top: 150px;
    margin: 0;
    padding: 0;
    list-style: none;
    color: var(--text-light);
    font-size: 11.5px;
  }
  .contact-list li {
    display: flex;
    align-items: center;
    gap: 8px;
    height: 22px;
  }
  .contact-icon { width: 13px; height: 13px; flex: none; }
  .address {
    position: absolute;
    left: 172px;
    top: 214px;
    margin: 0;
    font-style: normal;
    color: var(--text-light);
    font-size: 11.5px;
    line-height: 1.7;
  }
  .brand {
    display: flex;
    align-items: center;
    gap: 10px;
    font-weight: 600;
    letter-spacing: 1px;
  }
  .brand-front {
    position: absolute;
    left: 345px;
    top: 128px;
    color: var(--ink-grey);
    font-size: 30px;
  }
  .brand-back {
    color: var(--text-light);
    font-size: 46px;
  }
  .brand-dot {
    width: 14px; height: 14px; border-radius: 50%;
    background: var(--teal);
  }
  .brand-back .brand-dot { width: 20px; height: 20px; background: var(--text-light); }
</style>
</head>
<body>
<main class="stage">
  <section class="card card-front" aria-label="Card front">
    <svg class="front-shapes" width="530" height="303" viewBox="0 0 530 303">
      <path d="M0,52 C230,40 332,150 332,303" fill="none" stroke="var(--teal)" stroke-width="14"/>
      <path d="M0,70 C210,60 312,160 312,303 L0,303 Z" fill="var(--card-grey)" stroke="var(--card-white)" stroke-width="5"/>
    </svg>

    <div class="holder">
      <p class="holder-name">Marek Holloway</p>
      <p class="holder-title">Managing Director</p>
    </div>

    <ul class="contact-list">
      <li>
        <svg class="contact-icon" viewBox="0 0 16 16"><circle cx="8" cy="8" r="7" fill="none" stroke="#fff" stroke-width="1.2"/><path d="M5.5 4.5 L7 6 L6.2 7 C6.8 8.3 7.7 9.2 9 9.8 L10 9 L11.5 10.5 L10.6 11.5 C7.6 11 5 8.4 4.5 5.4 Z" fill="#fff"/></svg>
        021.4827 390
      </li>
      <li>
        <svg class="contact-icon" viewBox="0 0 16 16"><circle cx="8" cy="8" r="7" fill="none" stroke="#fff" stroke-width="1.2"/><rect x="4.5" y="5.5" width="7" height="5" fill="none" stroke="#fff" stroke-width="1"/><path d="M4.5 5.5 L8 8.3 L11.5 5.5" fill="none" stroke="#fff" stroke-width="1"/></svg>
        info@korvane.com
      </li>
      <li>
        <svg class="contact-icon" viewBox="0 0 16 16"><circle cx="8" cy="8" r="7" fill="none" stroke="#fff" stroke-width="1.2"/><ellipse cx="8" cy="8" rx="3" ry="7" fill="none" stroke="#fff" stroke-width="1"/><path d="M1 8 H15 M2.5 4.5 H13.5 M2.5 11.5 H13.5" stroke="#fff" stroke-width="1"/></svg>
        www.korvane.com
      </li>
    </ul>

    <address class="address">
      48 Harbour Road<br>
      Suite 12,Brookvale<br>
      NSW 2100
    </address>

    <div class="brand brand-front">
      <span class="brand-dot"></span>
      <span class="brand-name">KORVANE</span>
    </div>
  </section>

  <section class="card card-back" aria-label="Card back">
    <div class="brand brand-back">
      <span class="brand-dot"></span>
      <span class="brand-name">KORVANE</span>
    </div>
  </section>
</main>
</body>
</html>
```